a business advisory consulting website

I need a website 3-5 pages to sell my professional services in IT and Project management Consulting. My company name is Tidewell Advisory Consulting. I want it to be device friendly and easy to navigate for the busy executive however intriguing enough.
I have attached some info I drafted on About the company and personal Bio. Also there is a website that I really like that I have attached the initial site pdf and websites that I like are here: https://quillmarkfunds.example, https://lumetratrends.example, https://www.corbelteachingconsulting.example as examples. Thanks
Updates

Hi Designers, I have uploaded the logo in 3D .png format, to assist in the web design.

Target Market(s)

B2B, governments, IT companies, Project Management companies and Consulting firms, small medium enterprises to large corporate enterprises.

Industry/Entity Type

It Professional

Coding

Coded - Design and coding required

Number of Pages Required

5+ page

Font styles to use
Sans Serif

Requirements
Must have
• Home, About company, the team, what we do and contact us
Nice to have
• Blog
Should not have
• pop ups, flash

```html
<!DOCTYPE html>
<html lang="en">
<head>
<meta charset="utf-8">
<title>Tidewell Advisory – Strategy and Management Consulting</title>
<link rel="stylesheet" href="https://fonts.googleapis.com/css2?family=Poppins:wght@400;500;600;700&family=Roboto:wght@500;700&display=swap">
<style>
:root{
  --navy:#232845;
  --navy-deep:#1b1f38;
  --red:#dd2428;
  --white:#ffffff;
  --ink:#2a2e45;
  --muted:#6b6f80;
  --line:#e4e4ec;
  --lavender:#e9e9f5;
}
*{box-sizing:border-box;margin:0;padding:0}
html,body{width:1200px;height:4209px;overflow:hidden}
body{position:relative;font-family:"Poppins",sans-serif;color:var(--ink);background:var(--white)}
section,header,footer{position:absolute;left:0;width:1200px}
.abs{position:absolute}
.brand-name{font-family:"Poppins",sans-serif;font-weight:700;color:var(--white);letter-spacing:.5px;line-height:1}

/* hero */
.hero{top:0;height:720px}
.hero-photo{position:absolute;inset:0;background:linear-gradient(100deg,#1f2a3a 0%,#34465c 35%,#2a3446 60%,#3c5266 100%)}
.hero-shape{position:absolute;left:0;top:0}
.site-logo{left:74px;top:44px;display:flex;align-items:center;gap:12px}
.site-logo .mark{width:22px;height:22px;background:var(--red)}
.site-logo .brand-name{font-size:27px;line-height:1.05}
.topbar{left:504px;top:20px;display:flex;align-items:center;color:var(--white);font-size:18px;font-weight:500}
.topbar .item{display:flex;align-items:center;gap:10px}
.topbar .sep{width:1px;height:26px;background:rgba(255,255,255,.5);margin:0 24px}
.social{display:flex;gap:10px}
.social span{width:26px;height:26px;border-radius:50%;background:rgba(255,255,255,.85)}
.nav-rule{left:455px;top:66px;width:672px;height:1px;background:rgba(255,255,255,.45)}
.main-nav{left:526px;top:94px;display:flex;align-items:center;color:var(--white);font-size:15px;font-weight:500}
.main-nav a{color:inherit;text-decoration:none}
.main-nav .active{text-decoration:underline;text-underline-offset:4px}
.main-nav .div{width:1px;height:16px;background:rgba(255,255,255,.6);margin:0 28px}
.hero-copy{left:0;width:1200px;top:262px;text-align:center;color:var(--white)}
.hero-copy h1{font-family:"Roboto",sans-serif;font-weight:700;font-size:50px;letter-spacing:1px;line-height:1.1}
.hero-copy p{font-size:33px;line-height:46px;margin-top:8px}
.btn{display:inline-flex;align-items:center;justify-content:center;gap:10px;color:var(--white);font-size:20px;font-weight:500}
.btn-red{background:var(--red)}
.btn-navy{background:var(--navy)}
.hero .btn{left:503px;top:451px;width:194px;height:51px;position:absolute}
.slider-arrow{width:46px;height:46px;border-radius:50%;display:flex;align-items:center;justify-content:center}
.arrow-outline{border:2px solid var(--navy)}
.arrow-red{background:var(--red)}
.hero .prev{left:114px;top:315px}
.hero .next{left:1042px;top:315px}
.dots{display:flex;gap:8px}
.dots span{width:11px;height:11px;border-radius:50%;border:1.5px solid #c9c9d2}
.dots span.on{background:var(--red);border-color:var(--red)}
.hero .dots{left:564px;top:632px}
.hero .dots span{border-color:rgba(255,255,255,.8)}

/* about */
.about{top:720px;height:540px}
.about-circle{left:123px;top:65px;width:320px;height:320px;border-radius:50%;border:1.5px solid #e5b7bb;display:flex;align-items:center;justify-content:center}
.about-circle .brand-name{color:var(--navy);font-size:34px;margin-right:70px}
.badge{left:378px;top:199px;width:170px;height:57px;background:var(--navy);color:var(--white);display:flex;align-items:center;gap:8px;padding-left:14px}
.badge strong{font-size:38px;font-weight:500;line-height:1}
.badge small{font-size:14px;line-height:1.1}
.dot-grid{background-image:radial-gradient(#c9cad6 1.6px,transparent 1.8px);background-size:14px 14px}
.about h2{left:613px;top:100px;font-size:42px;font-weight:600;color:var(--navy)}
.about .underline{left:615px;top:165px;width:60px;height:3px;background:var(--red)}
.about .lead{left:613px;top:182px;width:460px;font-size:20px;font-weight:600;line-height:30px;color:var(--navy)}
.about .body{left:613px;top:250px;width:460px;font-size:16px;line-height:30px;color:var(--muted)}
.about .btn{position:absolute;left:615px;top:393px;width:175px;height:50px;font-size:19px}

/* services */
.services{top:1260px;height:748px;overflow:hidden}
.services-photo{position:absolute;inset:0;background:linear-gradient(90deg,#9aa0ab 0%,#d9dce2 25%,#eef0f3 50%,#d8dbe1 75%,#a9a9ae 100%)}
.services h2{left:0;width:1200px;top:92px;text-align:center;font-size:40px;font-weight:600;color:var(--navy)}
.services .sub{left:0;width:1200px;top:150px;text-align:center;font-size:17px;font-weight:500;color:var(--navy)}
.hex{width:216px;height:248px;clip-path:polygon(50% 0,100% 25%,100% 75%,50% 100%,0 75%,0 25%);background:var(--navy);color:var(--white);display:flex;flex-direction:column;align-items:center;justify-content:center;text-align:center;font-size:17px;line-height:26px;gap:14px}
.hex.hot{background:var(--red)}
.hex svg{width:54px;height:54px}

/* value */
.value{top:2008px;height:592px;background:linear-gradient(180deg,#ffffff 0%,#f2f2f9 40%,var(--lavender) 100%)}
.section-title{left:0;width:1200px;text-align:center;font-family:"Roboto",sans-serif;font-weight:700;font-size:38px;color:var(--navy)}
.value .section-title{top:78px}
.value .underline{left:570px;top:140px;width:60px;height:3px;background:var(--red)}
.value-card{left:455px;top:180px;width:292px;height:314px;background:var(--white);box-shadow:0 6px 24px rgba(35,40,69,.08)}
.prop{top:224px;width:292px;text-align:center}
.prop .icon{width:85px;height:85px;margin:0 auto;background:var(--navy);border-radius:6px;display:flex;align-items:center;justify-content:center}
.prop .icon.red{background:var(--red)}
.prop h3{margin-top:22px;font-size:19px;line-height:26px;font-weight:700;color:var(--navy)}
.prop p{margin-top:14px;font-size:16px;line-height:26px;color:var(--muted)}

/* team */
.team{top:2595px;height:580px;overflow:hidden}
.team-photo{position:absolute;inset:0;background:linear-gradient(90deg,#2a3050 0%,#3b4262 45%,#2e3554 100%)}
.team h2{left:152px;top:200px;font-family:"Roboto",sans-serif;font-weight:700;font-size:40px;color:var(--white)}
.team .body{left:152px;top:256px;width:400px;font-size:16px;line-height:30px;color:var(--white)}
.team .prev{left:154px;top:371px;width:34px;height:34px;border-color:var(--white)}
.team .next{left:204px;top:371px;width:34px;height:34px}
.member{top:111px;width:195px;height:409px;background:var(--white);border-radius:98px 98px 60px 60px;text-align:center}
.member .photo{width:164px;height:164px;border-radius:50%;margin:15px auto 0;background:linear-gradient(180deg,#d7d9de,#9aa0ab)}
.member h3{margin-top:38px;font-size:18px;font-weight:500;color:var(--navy)}
.member p{margin-top:4px;font-size:13px;line-height:17px;color:var(--muted);padding:0 30px}
.member .go{position:absolute;left:75px;top:294px;width:46px;height:46px;border-radius:50%;background:var(--navy);display:flex;align-items:center;justify-content:center}

/* testimonials */
.testimonials{top:3175px;height:580px}
.testimonials .section-title{top:70px}
.testimonials .underline{left:570px;top:132px;width:60px;height:3px;background:linear-gradient(90deg,var(--red),#6b3fa0,var(--navy))}
.review{top:170px;width:301px;height:288px;border:1.5px solid var(--line);padding:30px 35px 0}
.stars{color:#f2b01e;font-size:20px;letter-spacing:2px;line-height:1}
.review h4{margin-top:10px;font-size:14px;font-weight:600;color:var(--navy)}
.review p{margin-top:12px;font-size:13px;line-height:22px;color:var(--muted)}
.reviewer{margin-top:32px;display:flex;align-items:center;gap:14px}
.reviewer .avatar{width:36px;height:36px;border-radius:50%;background:linear-gradient(180deg,#c9ccd4,#6c7080)}
.reviewer b{display:block;font-size:13px;font-weight:600;color:var(--navy)}
.reviewer span{display:block;font-size:12px;color:var(--muted)}
.testimonials .dots{left:564px;top:502px}

/* footer */
.site-footer{top:3755px;height:454px;overflow:hidden}
.site-footer .bg{position:absolute;left:0;top:0}
.site-footer .site-logo{left:74px;top:178px}
.footer-social{left:126px;top:285px;display:flex;gap:18px}
.footer-social span{width:18px;height:18px;border-radius:50%;background:rgba(255,255,255,.85)}
.footer-col{color:var(--white)}
.footer-col h5{font-size:16px;font-weight:600;margin-bottom:18px}
.contact-col{left:347px;top:132px}
.contact-col .row{display:flex;gap:18px;font-size:13px;line-height:20px;color:#cfd1dd;margin-bottom:14px}
.company-col{left:626px;top:132px}
.company-col a{display:block;font-size:13px;line-height:24.5px;color:#cfd1dd;text-decoration:none}
.cta-col{left:824px;top:132px;width:310px}
.cta-col p{font-size:14px;line-height:24px;color:#cfd1dd}
.cta-col .btn{margin-top:26px;width:193px;height:46px;font-size:18px}
.footer-rule{left:74px;top:360px;width:1052px;height:1px;background:rgba(255,255,255,.2)}
.copyright{left:74px;top:396px;font-size:15px;color:#cfd1dd}
.legal{left:872px;top:398px;display:flex;gap:30px;font-size:13px;color:#cfd1dd}
</style>
</head>
<body>

<header class="hero">
  <div class="hero-photo" role="img" aria-label="Businessman in a suit on the phone with a city skyline behind him"></div>
  <svg class="hero-shape" width="1200" height="720" viewBox="0 0 1200 720" aria-hidden="true">
    <polygon points="0,630 600,702 1200,630 1200,720 0,720" fill="#ffffff"/>
    <polygon points="0,640 600,710 600,720 0,650" fill="#232845"/>
    <polygon points="600,710 1200,640 1200,650 600,720" fill="#dd2428"/>
  </svg>

  <div class="abs site-logo"><span class="mark"></span><span class="brand-name">TIDEWELL<br>ADVISORY</span></div>

  <div class="abs topbar">
    <span class="item">
      <svg width="28" height="28" viewBox="0 0 28 28" fill="none" stroke="#fff" stroke-width="1.6"><circle cx="14" cy="14" r="12.5"/><path d="M10 8l2.5 3-1.5 1.5c.8 1.8 2.2 3.2 4 4l1.5-1.5 3 2.5-1.5 2c-4.5 0-9-4.5-9-9z"/></svg>
      +80 555 0142 77
    </span>
    <span class="sep"></span>
    <span class="item">
      <svg width="28" height="28" viewBox="0 0 28 28" fill="none" stroke="#fff" stroke-width="1.6"><circle cx="14" cy="14" r="12.5"/><rect x="8" y="10" width="12" height="8"/><path d="M8 10l6 5 6-5"/></svg>
      info@tidewell.example
    </span>
    <span class="sep"></span>
    <span class="social"><span></span><span></span><span></span></span>
  </div>
  <div class="abs nav-rule"></div>
  <nav class="abs main-nav">
    <a class="active" href="#">HOME</a><span class="div"></span>
    <a href="#">ABOUT US</a><span class="div"></span>
    <a href="#">TEAM</a><span class="div"></span>
    <a href="#">WHAT WE DO</a><span class="div"></span>
    <a href="#">CONTACT US</a>
  </nav>

  <div class="abs hero-copy">
    <h1>TIDEWELL ADVISORY</h1>
    <p>A strategy and Management<br>consulting enterprise.</p>
  </div>
  <a class="btn btn-red" href="#">Get Quote
    <svg width="26" height="12" viewBox="0 0 26 12" fill="none" stroke="#fff" stroke-width="1.8"><path d="M0 6h24M19 1l5 5-5 5"/></svg></a>

  <span class="abs slider-arrow arrow-outline prev"><svg width="14" height="20" viewBox="0 0 14 20" fill="none" stroke="#232845" stroke-width="2.2"><path d="M11 2L3 10l8 8"/></svg></span>
  <span class="abs slider-arrow arrow-red next"><svg width="14" height="20" viewBox="0 0 14 20" fill="none" stroke="#fff" stroke-width="2.2"><path d="M3 2l8 8-8 8"/></svg></span>

  <div class="abs dots"><span></span><span class="on"></span><span></span><span></span></div>
</header>

<section class="about">
  <div class="abs about-circle"><span class="brand-name">TIDEWELL</span></div>
  <div class="abs dot-grid" style="left:465px;top:158px;width:104px;height:142px"></div>
  <div class="abs badge"><strong>20</strong><small>Years<br>Experience</small></div>
  <div class="abs dot-grid" style="left:1138px;top:106px;width:62px;height:144px"></div>

  <h2 class="abs">Tidewell Advisory</h2>
  <span class="abs underline"></span>
  <p class="abs lead">A strategy consulting and financial advisory firm with a focus on Africa.</p>
  <p class="abs body">Lorem Ipsum has been the industry's standard dummy text ever since the 1500s Lorem Ipsum is simply dummy text of the printing and typesetting industry. Lorem Ipsum is simply dummy text of the printing and typesetting industry.</p>
  <a class="btn btn-navy" href="#">Learn More
    <svg width="24" height="12" viewBox="0 0 26 12" fill="none" stroke="#fff" stroke-width="1.8"><path d="M0 6h24M19 1l5 5-5 5"/></svg></a>
</section>

<section class="services">
  <div class="services-photo" role="img" aria-label="Colleagues talking in a bright office, seen on both sides of the service grid"></div>
  <svg class="abs" style="left:0;top:0" width="1200" height="100" viewBox="0 0 1200 100" aria-hidden="true">
    <polygon points="0,0 1200,0 1200,84 600,6 0,84" fill="#ffffff"/>
    <polygon points="0,84 600,6 600,15 0,92" fill="#232845"/>
    <polygon points="600,6 1200,84 1200,92 600,15" fill="#dd2428"/>
  </svg>
  <h2 class="abs">Services We Provide</h2>
  <p class="abs sub">In a complex world of IT, let us help simplify.</p>

  <div class="abs hex" style="left:141px;top:218px">
    <svg viewBox="0 0 54 54" fill="none" stroke="#fff" stroke-width="2.6"><circle cx="14" cy="10" r="4"/><circle cx="40" cy="30" r="4"/><path d="M14 16v30M8 40l6 6 6-6M40 24c0-8-10-4-10-12"/></svg>
    <span>Strategy<br>Analytics</span>
  </div>
  <div class="abs hex hot" style="left:374px;top:218px">
    <svg viewBox="0 0 54 54" fill="#fff"><circle cx="30" cy="17" r="11"/><path d="M4 38h10l10 4h12l12-8 2 3-14 11H20l-8-3H4z"/></svg>
    <span>Market<br>Entry</span>
  </div>
  <div class="abs hex" style="left:608px;top:218px">
    <svg viewBox="0 0 54 54" fill="none" stroke="#fff" stroke-width="2.6"><rect x="11" y="4" width="32" height="46" rx="3"/><rect x="16" y="10" width="22" height="10"/><path d="M17 28h5M25 28h5M33 28h5M17 35h5M25 35h5M33 35h5M17 42h5M25 42h5M33 42h5"/></svg>
    <span>Accounting &amp;<br>Insurance</span>
  </div>
  <div class="abs hex" style="left:842px;top:218px">
    <svg viewBox="0 0 54 54" fill="none" stroke="#fff" stroke-width="2.6"><path d="M20 34c0-16 12-26 28-28-2 16-12 28-28 28z"/><circle cx="36" cy="18" r="4"/><path d="M20 34l-8 8M24 38l-6 10M16 30L6 36"/></svg>
    <span>Advise for Early<br>Stage Startups</span>
  </div>
  <div class="abs hex" style="left:258px;top:418px">
    <svg viewBox="0 0 54 54" fill="#fff"><rect x="8" y="32" width="6" height="14"/><rect x="18" y="26" width="6" height="20"/><rect x="28" y="30" width="6" height="16"/><rect x="38" y="20" width="6" height="26"/><path d="M8 24l12-10 10 6 14-12" stroke="#fff" stroke-width="2.6" fill="none"/><rect x="4" y="46" width="46" height="3"/></svg>
    <span>Finance<br>Services</span>
  </div>
  <div class="abs hex" style="left:492px;top:418px">
    <svg viewBox="0 0 54 54" fill="#fff"><path d="M24 8a20 20 0 1 0 20 22H24z"/><path d="M28 4a20 20 0 0 1 20 20H28z"/></svg>
    <span>Business Process<br>Optimization</span>
  </div>
  <div class="abs hex" style="left:726px;top:418px">
    <svg viewBox="0 0 54 54" fill="#fff"><circle cx="27" cy="16" r="7"/><circle cx="12" cy="20" r="5"/><circle cx="42" cy="20" r="5"/><path d="M15 40c0-8 5-13 12-13s12 5 12 13z"/><path d="M4 36c0-6 3-9 8-9 2 0 4 1 5 2-2 2-3 5-3 7z"/><path d="M50 36c0-6-3-9-8-9-2 0-4 1-5 2 2 2 3 5 3 7z"/></svg>
    <span>Managed<br>Services</span>
  </div>
</section>

<section class="value">
  <h2 class="abs section-title">OUR VALUE PROPOSITION</h2>
  <span class="abs underline"></span>
  <div class="abs value-card"></div>

  <div class="abs prop" style="left:145px">
    <div class="icon"><svg width="46" height="52" viewBox="0 0 46 52" fill="none" stroke="#fff" stroke-width="2.4"><rect x="8" y="4" width="30" height="40" rx="2"/><path d="M23 12l7 3v5c0 4-3 7-7 8-4-1-7-4-7-8v-5z"/><path d="M14 34h18M4 44c0 4 3 6 6 6h28"/></svg></div>
    <h3>ETHICS &amp;<br>INTEGRITY</h3>
    <p>the printing and typesetting<br>industry. Lorem Ipsum</p>
  </div>
  <div class="abs prop" style="left:455px">
    <div class="icon red"><svg width="46" height="52" viewBox="0 0 46 52" fill="none" stroke="#fff" stroke-width="2.4"><circle cx="23" cy="20" r="14"/><path d="M16 20l5 5 9-9M14 32l-4 16 8-4 5 6M32 32l4 16-8-4-5 6"/></svg></div>
    <h3>EFFFICIENCY &amp;<br>EFFECTIVENESS.</h3>
    <p>the printing and typesetting<br>industry. Lorem Ipsum</p>
  </div>
  <div class="abs prop" style="left:765px">
    <div class="icon"><svg width="56" height="44" viewBox="0 0 56 44" fill="#fff"><circle cx="28" cy="12" r="8"/><circle cx="12" cy="16" r="6"/><circle cx="44" cy="16" r="6"/><path d="M14 40c0-10 6-16 14-16s14 6 14 16z"/><path d="M2 36c0-7 4-11 10-11 2 0 4 1 5 2-3 3-4 6-4 9z"/><path d="M54 36c0-7-4-11-10-11-2 0-4 1-5 2 3 3 4 6 4 9z"/></svg></div>
    <h3>GROW &amp;<br>SCALE</h3>
    <p>the printing and typesetting<br>industry. Lorem Ipsum</p>
  </div>
</section>

<section class="team">
  <div class="team-photo" role="img" aria-label="Team of consultants meeting around a table, under a dark navy overlay"></div>
  <svg class="abs" style="left:0;top:0" width="1200" height="100" viewBox="0 0 1200 100" aria-hidden="true">
    <polygon points="0,0 1200,0 1200,82 600,5 0,82" fill="#eaeaf5"/>
    <polygon points="0,82 600,5 600,14 0,90" fill="#232845"/>
    <polygon points="600,5 1200,82 1200,90 600,14" fill="#dd2428"/>
  </svg>
  <h2 class="abs">MEET OUR TEAM</h2>
  <p class="abs body">Lorem Ipsum is simply dummy text of the printing and typesetting industry. Lorem Ipsum has been the industry's standard dummy text</p>
  <span class="abs slider-arrow arrow-outline prev"><svg width="10" height="16" viewBox="0 0 10 16" fill="none" stroke="#fff" stroke-width="2"><path d="M8 2L2 8l6 6"/></svg></span>
  <span class="abs slider-arrow arrow-red next"><svg width="10" height="16" viewBox="0 0 10 16" fill="none" stroke="#fff" stroke-width="2"><path d="M2 2l6 6-6 6"/></svg></span>

  <article class="abs member" style="left:590px">
    <div class="photo" role="img" aria-label="Portrait of Daniel Kiprono"></div>
    <h3>Daniel Kiprono</h3>
    <p>Managing Principal</p>
    <span class="go"><svg width="22" height="12" viewBox="0 0 22 12" fill="none" stroke="#fff" stroke-width="1.8"><path d="M0 6h20M15 1l5 5-5 5"/></svg></span>
  </article>
  <article class="abs member" style="left:829px">
    <div class="photo" role="img" aria-label="Portrait of Marcus Otieno"></div>
    <h3>Marcus Otieno</h3>
    <p>Management Consultant</p>
    <span class="go"><svg width="22" height="12" viewBox="0 0 22 12" fill="none" stroke="#fff" stroke-width="1.8"><path d="M0 6h20M15 1l5 5-5 5"/></svg></span>
  </article>
</section>

<section class="testimonials">
  <h2 class="abs section-title">TESTIMONIAL</h2>
  <span class="abs underline"></span>

  <article class="abs review" style="left:129px">
    <div class="stars">★★★★★</div>
    <h4>"SOLID Service! Vety consistent!"</h4>
    <p>the printing and typesetting industry. Lorem Ipsum has been the industry's standard dummy text ever since the 1500s Lorem Ipsum!</p>
    <div class="reviewer"><span class="avatar"></span><div><b>Colin Marsh</b><span>Web Development</span></div></div>
  </article>
  <article class="abs review" style="left:455px">
    <div class="stars">★★★★★</div>
    <h4>"SOLID Service! Vety consistent!"</h4>
    <p>the printing and typesetting industry. Lorem Ipsum has been the industry's standard dummy text ever since the 1500s Lorem Ipsum!</p>
    <div class="reviewer"><span class="avatar"></span><div><b>Colin Marsh</b><span>Web Development</span></div></div>
  </article>
  <article class="abs review" style="left:777px">
    <div class="stars">★★★★★</div>
    <h4>"SOLID Service! Vety consistent!"</h4>
    <p>the printing and typesetting industry. Lorem Ipsum has been the industry's standard dummy text ever since the 1500s Lorem Ipsum!</p>
    <div class="reviewer"><span class="avatar"></span><div><b>Colin Marsh</b><span>Web Development</span></div></div>
  </article>

  <div class="abs dots"><span></span><span class="on"></span><span></span><span></span></div>
</section>

<footer class="site-footer">
  <svg class="bg" width="1200" height="454" viewBox="0 0 1200 454" aria-hidden="true">
    <rect x="0" y="0" width="1200" height="454" fill="#232845"/>
    <polygon points="0,0 1200,0 1200,78 600,5 0,78" fill="#ffffff"/>
    <polygon points="0,78 600,5 600,13 0,86" fill="#232845"/>
    <polygon points="600,5 1200,78 1200,86 600,13" fill="#dd2428"/>
  </svg>

  <div class="abs site-logo"><span class="mark"></span><span class="brand-name">TIDEWELL<br>ADVISORY</span></div>
  <div class="abs footer-social"><span></span><span></span><span></span></div>

  <div class="abs footer-col contact-col">
    <h5>Contact Us</h5>
    <div class="row"><svg width="16" height="20" viewBox="0 0 16 20" fill="none" stroke="#fff" stroke-width="1.6"><path d="M8 19s7-7 7-11A7 7 0 0 0 1 8c0 4 7 11 7 11z"/><circle cx="8" cy="8" r="2.5"/></svg><span>240 Harbor Lane #8<br>Austin 73301 TX</span></div>
    <div class="row"><svg width="18" height="18" viewBox="0 0 18 18" fill="#fff"><path d="M3 1l4 4-2 2c1 2 3 4 5 5l2-2 4 4-2 3C7 17 1 11 1 3z"/></svg><span>(555) 014-2290</span></div>
    <div class="row"><svg width="18" height="14" viewBox="0 0 18 14" fill="none" stroke="#fff" stroke-width="1.6"><rect x="1" y="1" width="16" height="12"/><path d="M1 1l8 7 8-7"/></svg><span>hello@tidewell.example</span></div>
  </div>

  <div class="abs footer-col company-col">
    <h5>Company</h5>
    <a href="#">Home</a><a href="#">About</a><a href="#">Why Tidewell</a><a href="#">Services</a><a href="#">Testimonials</a><a href="#">Contact Us</a>
  </div>

  <div class="abs footer-col cta-col">
    <h5>Stil have questions?</h5>
    <p>Contact us usig this form. A repesenta-tive will aswer your questions as soon as possible.</p>
    <a class="btn btn-red" href="#">Get In Touch
      <svg width="24" height="12" viewBox="0 0 26 12" fill="none" stroke="#fff" stroke-width="1.8"><path d="M0 6h24M19 1l5 5-5 5"/></svg></a>
  </div>

  <div class="abs footer-rule"></div>
  <p class="abs copyright">Copyright 2020 Tidewell Advisory. All Rights Reserved.</p>
  <div class="abs legal"><span>Privacy Policy</span><span>Terms Of Services</span></div>
</footer>

</body>
</html>
```